Velvet Jubilee Flyer

I need an 8.5x11 or 8.5x14 or 11x17 flyer for a benefit concert. Logo has already been designed; uploading several different versions, and you could choose which you want to use. For flyer design: something subtly musical (not a big fan of using musical symbols in the design, treble clefs, eighth notes, etc.) But something classy. I'm uploading unformatted copy, and two logos: one of the radio station that is helping to sponsor the event, and one for the organization the concert is benefitting. This is quick turnaround, so I promise to be very responsive with feedback. Thanks!

```html
<!DOCTYPE html>
<html lang="en">
<head>
<meta charset="utf-8">
<title>Midwinter Velvet Jubilee – Flyer</title>
<link rel="stylesheet" href="https://fonts.googleapis.com/css2?family=Fredoka:wght@600;700&family=Quicksand:wght@500;600;700&display=swap">
<style>
  :root {
    --page-bg: #eceef2;
    --night-top: #1a2070;
    --night-mid: #2233a6;
    --night-low: #2c52d4;
    --snow: #ffffff;
    --pink: #f2568f;
    --yellow: #ecf05a;
    --teal: #52dcd2;
    --sky-text: #8feae6;
    --white-text: #ffffff;
    --ink: #1a1a1a;
    --magenta: #c0288a;
    --muted: #666666;
    --title-font: "Fredoka", sans-serif;
    --body-font: "Quicksand", sans-serif;
  }
  * { box-sizing: border-box; margin: 0; padding: 0; }
  html, body {
    width: 1200px; height: 605px; overflow: hidden;
    background: var(--page-bg);
  }
  .flyer {
    position: absolute; left: 375px; top: 10px;
    width: 450px; height: 585px; overflow: hidden;
    background: linear-gradient(180deg, var(--night-top) 0%, var(--night-mid) 45%, var(--night-low) 100%);
    box-shadow: 0 6px 18px rgba(0,0,0,.25);
    font-family: var(--body-font);
  }
  .layer { position: absolute; left: 0; top: 0; width: 450px; height: 585px; }
  .title-text { font-family: var(--title-font); font-weight: 700; }
  .fill-pink { fill: var(--pink); }
  .fill-yellow { fill: var(--yellow); }
  .fill-teal { fill: var(--teal); }

  .date {
    position: absolute; left: 0; right: 0; top: 166px; text-align: center;
    color: var(--white-text); font-weight: 700; font-size: 19px;
  }
  .time {
    position: absolute; left: 0; right: 0; top: 192px; text-align: center;
    color: var(--sky-text); font-weight: 600; font-size: 16px;
  }
  .tree-art {
    position: absolute; left: 10px; top: 228px; width: 186px; height: 196px;
    border-radius: 48% 48% 30% 30% / 52% 52% 30% 30%;
    background: radial-gradient(ellipse at 50% 45%, rgba(255,255,255,.42), rgba(255,255,255,.14) 65%, rgba(255,255,255,0) 100%);
  }
  .venue {
    position: absolute; left: 216px; top: 250px;
    color: var(--white-text); font-weight: 700; font-size: 18px; line-height: 24px;
  }
  .rooms {
    position: absolute; left: 216px; top: 336px;
    color: var(--sky-text); font-weight: 600; font-size: 14px; line-height: 20px;
  }

  .beneficiary {
    position: absolute; left: 28px; top: 436px; width: 160px;
    display: flex; flex-direction: column; align-items: center; gap: 12px;
  }
  .mark-square { width: 52px; height: 52px; background: var(--ink); }
  .beneficiary .org-name {
    color: var(--ink); font-weight: 700; font-size: 17px; text-align: center; line-height: 1.15;
  }
  .sponsor {
    position: absolute; left: 222px; top: 478px; width: 156px; text-align: center;
  }
  .sponsor .label { color: var(--magenta); font-weight: 700; font-size: 14px; margin-bottom: 8px; }
  .sponsor .station { display: flex; align-items: center; justify-content: center; gap: 7px; }
  .sponsor .station-mark { width: 18px; height: 18px; background: var(--magenta); flex: none; }
  .sponsor .station-name {
    color: var(--ink); font-weight: 700; font-size: 14px; line-height: 1.15; text-align: left;
  }
  .sponsor .web { color: var(--muted); font-weight: 600; font-size: 9px; margin-top: 4px; }
</style>
</head>
<body>
  <main class="flyer">
    <svg class="layer stars" viewBox="0 0 450 585" aria-hidden="true">
      <defs>
        <path id="sparkle" d="M0 -6 L1.2 -1.2 L6 0 L1.2 1.2 L0 6 L-1.2 1.2 L-6 0 L-1.2 -1.2 Z" fill="#fff"/>
      </defs>
      <use href="#sparkle" x="399" y="36"/>
      <use href="#sparkle" x="27" y="161"/>
      <use href="#sparkle" x="240" y="160"/>
      <use href="#sparkle" x="385" y="293"/>
      <use href="#sparkle" x="385" y="430"/>
      <g fill="#fff" opacity=".85">
        <circle cx="18" cy="22" r="1.3"/><circle cx="60" cy="40" r="1"/>
        <circle cx="40" cy="95" r="1.2"/><circle cx="150" cy="14" r="1"/>
        <circle cx="320" cy="18" r="1.2"/><circle cx="430" cy="80" r="1.3"/>
        <circle cx="380" cy="150" r="1"/><circle cx="430" cy="200" r="1.2"/>
        <circle cx="95" cy="180" r="1"/><circle cx="340" cy="215" r="1.2"/>
        <circle cx="420" cy="250" r="1"/><circle cx="285" cy="238" r="1"/>
        <circle cx="205" cy="235" r="1.2"/><circle cx="410" cy="340" r="1"/>
        <circle cx="300" cy="395" r="1.2"/><circle cx="425" cy="395" r="1"/>
        <circle cx="210" cy="400" r="1"/><circle cx="350" cy="370" r="1.2"/>
        <circle cx="15" cy="230" r="1"/><circle cx="120" cy="215" r="1"/>
      </g>
    </svg>

    <svg class="layer title" viewBox="0 0 450 585" role="heading" aria-level="1" aria-label="Midwinter Velvet Jubilee">
      <text class="title-text fill-pink" x="88" y="145" font-size="158" textLength="86" lengthAdjust="spacingAndGlyphs">M</text>
      <text class="title-text fill-pink" x="178" y="59" font-size="32" textLength="186" lengthAdjust="spacingAndGlyphs">IDWINTER</text>
      <text class="title-text" x="180" y="115" font-size="66" textLength="184" lengthAdjust="spacingAndGlyphs"><tspan class="fill-yellow">V</tspan><tspan class="fill-teal">E</tspan><tspan class="fill-pink">L</tspan><tspan class="fill-yellow">V</tspan><tspan class="fill-teal">E</tspan><tspan class="fill-pink">T</tspan></text>
      <text class="title-text fill-pink" x="180" y="145" font-size="33" textLength="184" lengthAdjust="spacingAndGlyphs">JUBILEE</text>
    </svg>

    <p class="date">Saturday ~ January 13, 2018</p>
    <p class="time">10am to 10pm</p>

    <div class="tree-art" role="img" aria-label="White silhouette of a bare winter tree standing on the snow"></div>

    <p class="venue">St. Ansel's United<br>Community Church<br>Rio Vista, NM</p>
    <p class="rooms">Music Building<br>Sanctuary</p>

    <svg class="layer snow" viewBox="0 0 450 585" aria-hidden="true">
      <path d="M0 416 C150 418 330 444 450 478 L450 585 L0 585 Z" fill="var(--snow)"/>
    </svg>

    <div class="beneficiary">
      <div class="mark-square"></div>
      <p class="org-name">Harbor Light<br>Care Network</p>
    </div>

    <div class="sponsor">
      <p class="label">Sponsored By:</p>
      <div class="station">
        <span class="station-mark"></span>
        <span class="station-name">Meridian<br>Classical Radio</span>
      </div>
      <p class="web">meridianclassical.org</p>
    </div>
  </main>
</body>
</html>
```